Business Card for a mobile physiotherapy company

I need a layout for a business card for a mobile physiotherapy company.
Slogan is "Mobile Physiotherapy - Your Road To Recovery"
Phone number is 867-402-5913
Email VantrePhysio@mailbright.ca (subject to change with website)
Website www.VantrePhysio.ca
My name and credentials: Kent Vantre Kent Vantre, BSc(kin), MPT, CAFCI, IMS
Information maybe included: Direct Billing, Services including Physiotherapy, IMS, acupuncture
Maybe include facebook and instagram logos
One side with the logo clean and sharp
Other side with details, try not to look too busy, keep everything concise

```html
<!DOCTYPE html>
<html lang="en">
<head>
<meta charset="utf-8">
<title>Vantre Therapy – Business Card</title>
<link rel="stylesheet" href="https://fonts.googleapis.com/css2?family=Open+Sans:ital,wght@0,400;0,600;0,700;1,400&display=swap">
<style>
  :root {
    --navy: #1d4a7d;
    --green: #0b5d49;
    --green-dark: #094c3c;
    --paper: #ffffff;
    --backdrop: #e9edf0;
    --text-navy: #1f4778;
  }
  * { margin: 0; padding: 0; box-sizing: border-box; }
  html, body { width: 1200px; height: 900px; overflow: hidden; }
  body {
    background: var(--backdrop);
    font-family: "Open Sans", Arial, sans-serif;
    display: flex;
    flex-direction: column;
    align-items: center;
    justify-content: center;
    gap: 40px;
  }
  .card {
    position: relative;
    width: 630px;
    height: 360px;
    background: var(--paper);
    box-shadow: 0 6px 18px rgba(0, 0, 0, 0.15);
    overflow: hidden;
  }

  /* Logo side */
  .card--logo {
    display: flex;
    align-items: center;
    justify-content: center;
  }
  .wordmark {
    display: flex;
    align-items: center;
    gap: 16px;
    color: var(--green);
    font-weight: 700;
    font-size: 52px;
    letter-spacing: 3px;
    text-transform: uppercase;
  }
  .wordmark__dot {
    width: 26px; height: 26px;
    border-radius: 50%;
    background: var(--navy);
  }

  /* Details side */
  .brand {
    position: absolute;
    top: 46px;
    right: 40px;
    display: flex;
    align-items: center;
    gap: 10px;
    color: var(--green);
    font-weight: 700;
    font-size: 28px;
    letter-spacing: 2px;
    text-transform: uppercase;
  }
  .brand__dot {
    width: 16px; height: 16px;
    border-radius: 50%;
    background: var(--navy);
  }
  .social {
    position: absolute;
    top: 168px;
    right: 48px;
    display: flex;
    gap: 8px;
  }
  .social__chip {
    width: 22px; height: 22px;
    border-radius: 50%;
    background: var(--navy);
  }
  .person {
    position: absolute;
    left: 40px;
    top: 118px;
  }
  .person__name {
    color: var(--green);
    font-weight: 700;
    font-size: 30px;
    line-height: 1.1;
  }
  .person__credentials {
    color: var(--text-navy);
    font-size: 15px;
    margin-top: 2px;
  }
  .contacts {
    position: absolute;
    left: 40px;
    top: 198px;
    list-style: none;
  }
  .contacts__item {
    display: flex;
    align-items: center;
    gap: 10px;
    color: var(--text-navy);
    font-size: 15px;
    height: 26px;
  }
  .contacts__icon { width: 22px; height: 22px; flex: none; }
  .slogan-band {
    position: absolute;
    left: 0; right: 0;
    top: 282px;
    height: 30px;
    background: var(--green);
    color: #fff;
    font-style: italic;
    font-size: 14px;
    display: flex;
    align-items: center;
    justify-content: center;
  }
  .services {
    position: absolute;
    left: 0; right: 0;
    top: 312px;
    height: 32px;
    color: var(--text-navy);
    font-style: italic;
    font-size: 13.5px;
    display: flex;
    align-items: center;
    justify-content: center;
  }
  .base-stripe {
    position: absolute;
    left: 0; right: 0; bottom: 0;
    height: 16px;
    background: var(--green);
  }
</style>
</head>
<body>

  <section class="card card--logo" aria-label="Logo side">
    <div class="wordmark"><span class="wordmark__dot"></span>Vantre Therapy</div>
  </section>

  <section class="card card--details" aria-label="Details side">
    <div class="brand"><span class="brand__dot"></span>Vantre Therapy</div>
    <div class="social" aria-label="Social media">
      <span class="social__chip"></span>
      <span class="social__chip"></span>
    </div>

    <div class="person">
      <h1 class="person__name">Kent Vantre</h1>
      <p class="person__credentials">BSc(Kin), MPT, CAFCI, IMS</p>
    </div>

    <ul class="contacts">
      <li class="contacts__item">
        <svg class="contacts__icon" viewBox="0 0 24 24" aria-hidden="true">
          <polygon points="12,1 22,6.5 22,17.5 12,23 2,17.5 2,6.5" fill="var(--green)"/>
          <path d="M7 9.5c0-1.3 2-2.3 5-2.3s5 1 5 2.3v1h-2.3v-1.2h-5.4v1.2H7z M8.5 11.5h7l1 5h-9z" fill="#fff"/>
        </svg>
        867-402-5913
      </li>
      <li class="contacts__item">
        <svg class="contacts__icon" viewBox="0 0 24 24" aria-hidden="true">
          <polygon points="12,1 22,6.5 22,17.5 12,23 2,17.5 2,6.5" fill="var(--green)"/>
          <rect x="6.5" y="8" width="11" height="8" fill="#fff"/>
          <polyline points="6.5,8 12,12.5 17.5,8" fill="none" stroke="var(--green)" stroke-width="1.2"/>
        </svg>
        VantrePhysio@mailbright.ca
      </li>
      <li class="contacts__item">
        <svg class="contacts__icon" viewBox="0 0 24 24" aria-hidden="true">
          <polygon points="12,1 22,6.5 22,17.5 12,23 2,17.5 2,6.5" fill="var(--green)"/>
          <g fill="none" stroke="#fff" stroke-width="1.2">
            <circle cx="12" cy="12" r="5.5"/>
            <ellipse cx="12" cy="12" rx="2.3" ry="5.5"/>
            <line x1="6.5" y1="12" x2="17.5" y2="12"/>
          </g>
        </svg>
        www.VantrePhysio.ca
      </li>
    </ul>

    <div class="slogan-band">Mobile Physiotherapy - Your Road To Recovery</div>
    <div class="services">Direct Billing, Services including Physiotherapy, IMS, Acupuncture</div>
    <div class="base-stripe"></div>
  </section>

</body>
</html>
```